Keen Compass - Web Design Project

We need a website for our new company based in Sao Paulo - Brazil. Our initial product is Keen Compass - an online assessment system based on the most recent neuroscience academic research. The system gathers tests that are applied in the selection and evaluation of employees. We would like to see designs that use the colors black and blue. The final design should communicate trust. We like clean and simple designs.

Login to www.keencompass-example.com.br
login: user
pass: user

We need three pages:
1- Login page: http://www.keencompass-example.com.br/

2- Welcome page: http://www.keencompass-example.com.br/sys/admin/index.php

3- Results page: http://www.keencompass-example.com.br/sys/admin/admin_provas_resultados.php?unique_id=5

Our logo was created using ArtLoomly.
Next projetcs: Tests interface redesign.

Industry/Entity Type

It Company

Requirements
Must have
• Link folders. i.e.:
Home :: Users :: John Doe :: Test1
Nice to have
• Image Buttons
Should not have
• Noise

```html
<!DOCTYPE html>
<html lang="en">
<head>
<meta charset="utf-8">
<title>Keen Compass — Proofs</title>
<link href="https://fonts.googleapis.com/css2?family=Source+Sans+3:ital,wght@0,300;0,400;0,600;0,700;1,300;1,600&display=swap" rel="stylesheet">
<style>
:root{
  --blue:#0a73a8;
  --blue-dark:#034b75;
  --blue-text:#2a86c4;
  --ink:#222;
  --grey-text:#555;
  --line:#d4d8dc;
  --row-a:#f1f1f1;
  --row-b:#e9f0f4;
  --footer:#efeded;
}
*{margin:0;padding:0;box-sizing:border-box}
html,body{width:1200px;height:1062px;overflow:hidden}
body{font-family:"Source Sans 3",sans-serif;background:#fff;position:relative;color:var(--ink)}
.topline{position:absolute;left:0;top:0;width:1200px;height:5px;background:#b9b9b9}
.header{position:absolute;left:0;top:5px;width:1200px;height:91px;background:linear-gradient(#fff,#e9e9e9)}
.brand{position:absolute;left:104px;top:40px;display:flex;align-items:center;gap:10px;font-size:28px;font-weight:400;color:var(--ink)}
.brand .dot{width:14px;height:14px;border-radius:50%;background:var(--blue)}
.nav{position:absolute;top:0;right:112px;display:flex;height:91px}
.nav a{display:flex;flex-direction:column;align-items:center;justify-content:center;gap:4px;padding:0 31px;font-size:14px;color:#444;text-decoration:none;border-left:1px solid #d8d8d8}
.nav a:first-child{border-left:none}
.nav a.active{color:var(--blue-text)}
.nav svg{width:20px;height:20px}
.crumbs{position:absolute;left:0;top:96px;width:1200px;height:28px;background:linear-gradient(#1a88bd,#04597f);border-bottom:1px solid #023e5c;color:#fff;font-size:11px;padding:6px 0 0 94px}
.stage{position:absolute;left:0;top:124px;width:1200px;height:90px;background:linear-gradient(#e4e4e4,#fff)}
.hero{position:absolute;left:98px;top:141px;width:1004px;height:434px;box-shadow:0 8px 10px -6px rgba(0,0,0,.45);overflow:hidden}
.hero-photo{position:absolute;inset:0;background:linear-gradient(90deg,#6e6a66 0%,#9c8d80 25%,#e8e4da 50%,#f6f2e8 65%,#c9d1db 85%,#8c9fb6 100%)}
.hero h2{position:absolute;left:470px;top:175px;font-weight:300;font-style:italic;font-size:38px;color:#111}
.hero h3{position:absolute;left:576px;top:228px;font-weight:300;font-style:italic;font-size:38px;color:var(--blue-text)}
.cta{position:absolute;left:683px;top:298px;width:161px;height:38px;border-radius:3px;background:linear-gradient(#1d8fc7,#034f7a);color:#fff;font-style:italic;font-weight:600;font-size:24px;padding:2px 0 0 11px}
.cta span{position:absolute;right:8px;top:5px;width:26px;height:26px;border-radius:50%;background:#0b2b40}
.cta svg{position:absolute;left:8px;top:7px}
.arrow{position:absolute;width:52px;height:56px;border-radius:50%;background:rgba(85,75,70,.85)}
.arrow svg{position:absolute;left:19px;top:18px}
.rule{position:absolute;left:93px;top:605px;width:977px;height:1px;background:#e0e0e0}
.title{position:absolute;left:99px;top:608px;font-size:33px;font-weight:400;color:var(--blue-text)}
.panel{position:absolute;left:102px;top:662px;width:960px}
.panel-head{height:40px;border-radius:4px 4px 0 0;background:linear-gradient(#1b8cc3,#03507c);color:#fff;display:flex;justify-content:space-between;align-items:center;padding:0 14px}
.panel-head strong{font-size:18px;font-weight:700}
.panel-head a{color:#fff;font-size:12px;font-weight:700;text-decoration:underline}
table{width:960px;border-collapse:collapse;border:1px solid var(--line)}
th,td{border-right:1px solid var(--line);border-bottom:1px solid var(--line)}
th{height:33px;background:#eef2f5;font-size:12px;font-weight:400;color:#222}
td{font-size:12.5px;color:var(--grey-text)}
td.name{color:var(--blue);padding-left:33px;width:218px}
td.tests{width:501px;padding:0 28px 0 65px;line-height:18px}
td.acts{padding-left:25px}
tr.r1 td{height:70px;background:linear-gradient(#fafafa,#e8e8e8)}
tr.r2 td{height:80px;background:var(--row-b)}
tr.r3 td{height:69px;background:linear-gradient(#fafafa,#e8e8e8)}
.btn{display:inline-block;width:88px;height:28px;line-height:28px;text-align:center;color:#fff;font-size:12px;font-weight:700;margin-right:6px;vertical-align:middle}
.btn.grey{background:linear-gradient(#9a9a9a,#676767);border:1px solid #ccc}
.btn.blue{background:linear-gradient(#1a88c0,#034f7a)}
.footer{position:absolute;left:0;top:968px;width:1200px;height:94px;background:var(--footer);color:#777;font-size:13px}
.footer .links{position:absolute;left:110px;top:20px}
.footer .copy{position:absolute;left:110px;top:52px}
.follow{position:absolute;left:913px;top:39px}
.sq{position:absolute;top:30px;width:32px;height:31px;background:#111}
.code{position:absolute;left:1116px;top:55px;font-size:12px;font-weight:700;color:#222}
</style>
</head>
<body>
<div class="topline"></div>
<header class="header">
  <div class="brand"><span class="dot"></span>Keen Compass</div>
  <nav class="nav">
    <a href="#"><svg viewBox="0 0 20 20"><path d="M2 10 10 3l8 7h-3v7H5v-7z" fill="#8a8a8a"/></svg>Home</a>
    <a href="#" class="active"><svg viewBox="0 0 20 20"><circle cx="10" cy="6" r="4" fill="#1b7fc0"/><path d="M3 12l7 6 7-6-7-2z" fill="#1b7fc0"/></svg>Provas</a>
    <a href="#"><svg viewBox="0 0 20 20"><circle cx="8" cy="12" r="5" fill="#8a8a8a"/><circle cx="15" cy="5" r="3" fill="#8a8a8a"/></svg>Usuários Configurações</a>
    <a href="#"><svg viewBox="0 0 20 20"><circle cx="10" cy="6" r="4" fill="#8a8a8a"/><path d="M3 18c0-5 3-7 7-7s7 2 7 7z" fill="#8a8a8a"/></svg>Logout</a>
  </nav>
</header>
<div class="crumbs">Home :: Users :: John Doe :: Test1</div>
<div class="stage"></div>
<section class="hero">
  <div class="hero-photo" role="img" aria-label="Photo of a smiling businessman in a suit with colleagues blurred in an office behind him"></div>
  <h2>Online Assessment</h2>
  <h3>For your needs....</h3>
  <div class="cta">Get Started<span><svg width="10" height="12" viewBox="0 0 10 12"><path d="M2 1l6 5-6 5z" fill="#fff"/></svg></span></div>
  <div class="arrow" style="left:18px;top:190px"><svg width="12" height="18" viewBox="0 0 12 18"><path d="M10 1 2 9l8 8z" fill="#fff"/></svg></div>
  <div class="arrow" style="left:940px;top:172px"><svg width="12" height="18" viewBox="0 0 12 18"><path d="M2 1l8 8-8 8z" fill="#fff"/></svg></div>
</section>
<div class="rule"></div>
<h1 class="title">Proofs</h1>
<section class="panel">
  <div class="panel-head"><strong>Latest products</strong><a href="#">View all products</a></div>
  <table>
    <tr><th>Name</th><th>Tests</th><th></th></tr>
    <tr class="r1"><td class="name">General</td><td class="tests">Urns Testing, Testing Balloons, Social Networks, Ultimatum Game V1, Pattern Recognition Test, Test Logic</td><td class="acts"><span class="btn grey">View Users</span><span class="btn blue">Results</span></td></tr>
    <tr class="r2"><td class="name">Unimerid</td><td class="tests">Urns Testing, Testing Balloons, Ultimatum Game V1, Test Pattern Recognition, Logic Test, Test Emotions, Information Sharing Strategic Test, Verbal Logic,</td><td class="acts"><span class="btn grey">View Users</span><span class="btn blue">Results</span></td></tr>
    <tr class="r3"><td class="name">Test1</td><td class="tests">Urns Testing, Testing Balloons, Social Networks, Ultimatum Game V1, Test Pattern Recognition, Logic Test, Test Prosody, Test Emotions, Information Sharing Strategic Test, Verbal Logic,</td><td class="acts"><span class="btn grey">View Users</span><span class="btn blue">Results</span></td></tr>
  </table>
</section>
<footer class="footer">
  <div class="links">Home &nbsp;|&nbsp; Testing &nbsp;|&nbsp; User &nbsp;|&nbsp; Settings &nbsp;|&nbsp; Logout</div>
  <div class="copy">Copyright © 2013 &nbsp;www.keencompass-example.com &nbsp;All rights reserved.</div>
  <div class="follow">Follow us on :</div>
  <div class="sq" style="left:1003px" aria-label="Social network link"></div>
  <div class="sq" style="left:1042px" aria-label="Social network link"></div>
  <div class="code">M1</div>
</footer>
</body>
</html>
```